Logo & Visitenkarte für Logopädische Praxis
Zielgruppe
In meiner logopädischen Praxis geht es um Sprach-, Sprech- und Stimmtherapie. Meine Zielgruppe sind Erwachsene jeglichen Alters und Geschlechts.
Aufgabenstellung
Ich habe noch keine konkreten Vorstellungen.

```html
<!DOCTYPE html>
<html lang="de">
<head>
<meta charset="utf-8">
<title>Fridolin Kuberz – Logopädische Praxis</title>
<link href="https://fonts.googleapis.com/css2?family=Ubuntu:wght@500;700&family=Open+Sans:wght@400;600&display=swap" rel="stylesheet">
<style>
  :root {
    --teal: #247f94;
    --green: #5f9a3a;
    --white: #ffffff;
    --stage: #ecebe8;
  }
  * { margin: 0; padding: 0; box-sizing: border-box; }
  html, body { width: 1200px; height: 968px; overflow: hidden; background: var(--stage); }
  .canvas { position: relative; width: 1200px; height: 968px; }
  .card {
    position: absolute; left: 335px; width: 530px; height: 340px;
    box-shadow: 0 6px 16px rgba(0,0,0,0.18);
    overflow: hidden;
  }
  .card--front { top: 84px; background: var(--teal); color: var(--white); }
  .card--back { top: 495px; background: var(--white); color: var(--teal); }
  .brand { position: absolute; left: 0; right: 0; text-align: center; }
  .brand__dot { display: block; margin: 0 auto; border-radius: 50%; }
  .card--front .brand { top: 80px; }
  .card--front .brand__dot { width: 118px; height: 118px; background: var(--white); }
  .card--back .brand { top: 26px; }
  .card--back .brand__dot { width: 98px; height: 98px; background: var(--teal); }
  .brand__name {
    font-family: "Ubuntu", sans-serif; font-weight: 700;
    font-size: 26px; letter-spacing: -0.3px; line-height: 1; margin-top: 24px;
  }
  .card--back .brand__name { font-size: 22px; margin-top: 18px; }
  .brand__tagline {
    font-family: "Ubuntu", sans-serif; font-weight: 700;
    font-size: 14px; letter-spacing: 6.4px; line-height: 1; margin-top: 9px;
  }
  .card--back .brand__tagline { font-size: 12px; letter-spacing: 5.4px; margin-top: 8px; }
  .wave { position: absolute; left: 0; top: 0; width: 530px; height: 340px; }
  .contact {
    position: absolute; display: flex; align-items: center; gap: 8px;
    font-family: "Open Sans", sans-serif; color: var(--white); font-size: 11px;
  }
  .contact__icon {
    width: 19px; height: 19px; border-radius: 50%; background: var(--white);
    display: flex; align-items: center; justify-content: center; flex: none;
  }
  .contact__icon svg { width: 12px; height: 12px; fill: var(--teal); }
  .contact--small { font-size: 8px; font-weight: 600; }
  .contact__address { font-size: 6px; font-weight: 600; line-height: 1.3; }
</style>
</head>
<body>
<main class="canvas">

  <section class="card card--front">
    <div class="brand">
      <span class="brand__dot"></span>
      <p class="brand__name">FRIDOLIN KUBERZ</p>
      <p class="brand__tagline">LOGOPÄDISCHE PRAXIS</p>
    </div>
  </section>

  <section class="card card--back">
    <div class="brand">
      <span class="brand__dot"></span>
      <p class="brand__name">FRIDOLIN KUBERZ</p>
      <p class="brand__tagline">LOGOPÄDISCHE PRAXIS</p>
    </div>

    <svg class="wave" viewBox="0 0 630 406" preserveAspectRatio="none" aria-hidden="true">
      <path fill="var(--teal)" d="M0,262 C180,305 380,252 545,228 C470,236 350,272 250,286 C150,298 60,290 0,276Z"/>
      <path fill="var(--green)" d="M0,290 C120,326 250,318 330,282 C245,308 120,314 0,298Z"/>
      <path fill="var(--teal)" d="M0,302 C120,330 260,322 380,282 C470,252 570,240 630,272 L630,406 L0,406Z"/>
    </svg>

    <div class="contact contact--small" style="left:16px; top:280px;">
      <span class="contact__icon"><svg viewBox="0 0 24 24"><path d="M12 2a10 10 0 1 0 0 20 10 10 0 0 0 0-20zm0 2c.9 0 2.2 1.7 2.8 5H9.2C9.8 5.7 11.1 4 12 4zM4.3 11h3.1c0 .7 0 1.4.1 2H4.3a8 8 0 0 1 0-2zm.6 4h2.8c.3 1.3.7 2.5 1.2 3.4A8 8 0 0 1 4.9 15zm2.8-6H4.9a8 8 0 0 1 4-3.4C8.4 6.5 8 7.7 7.7 9zM12 20c-.9 0-2.2-1.7-2.8-5h5.6c-.6 3.3-1.9 5-2.8 5zm3-7H9c-.1-.6-.1-1.3-.1-2h6.2c0 .7 0 1.4-.1 2zm.1 5.4c.5-.9.9-2.1 1.2-3.4h2.8a8 8 0 0 1-4 3.4zM16.6 13c.1-.6.1-1.3.1-2h3.1a8 8 0 0 1 0 2zm-.3-4c-.3-1.3-.7-2.5-1.2-3.4A8 8 0 0 1 19.1 9z"/></svg></span>
      www.logopraxis-kuberz.de
    </div>
    <div class="contact" style="left:16px; top:309px;">
      <span class="contact__icon"><svg viewBox="0 0 24 24"><path d="M12 2a7 7 0 0 0-7 7c0 5 7 13 7 13s7-8 7-13a7 7 0 0 0-7-7zm0 9.5A2.5 2.5 0 1 1 12 6.5a2.5 2.5 0 0 1 0 5z"/></svg></span>
      <p class="contact__address">Logopädische Therapiepraxis<br>Lene Havermann,<br>Lindenweg 27<br>45127 Essen</p>
    </div>

    <div class="contact" style="left:342px; top:241px;">
      <span class="contact__icon"><svg viewBox="0 0 24 24"><path d="M6.6 10.8a15 15 0 0 0 6.6 6.6l2.2-2.2c.3-.3.7-.4 1-.2 1.1.4 2.3.6 3.6.6.6 0 1 .4 1 1V20c0 .6-.4 1-1 1A17 17 0 0 1 3 4c0-.6.4-1 1-1h3.5c.6 0 1 .4 1 1 0 1.3.2 2.5.6 3.6.1.3 0 .7-.2 1z"/></svg></span>
      0201-555018
    </div>
    <div class="contact" style="left:342px; top:276px;">
      <span class="contact__icon"><svg viewBox="0 0 24 24"><path d="M6 3h12v5H6zM4 9h16a2 2 0 0 1 2 2v6h-4v4H6v-4H2v-6a2 2 0 0 1 2-2zm4 6v4h8v-4z"/></svg></span>
      0201-555019
    </div>
    <div class="contact contact--small" style="left:342px; top:312px;">
      <span class="contact__icon"><svg viewBox="0 0 24 24"><path d="M3 5h18v14H3zm2 2v.5l7 5 7-5V7zm0 3v7h14v-7l-7 5z"/></svg></span>
      info@logopraxis-kuberz.de
    </div>
  </section>

</main>
</body>
</html>
```